Business and Success Coaching Business Card

Need a business card for my coaching business. I coach small businesses, career professionals and, individuals wanting to unlock their human potential and achieve excellence. At the heart of our methodology is the Shaping Purposeful Action Routines Knowingly (SPARK) approach to formulate empowerment, create principles for success and setting achievable outcomes. I would like something that incorporates our new logo, something clean and sharp with a solid darker, but complementary background, color on the card front. The back should be white where there will be room for three questions

Target Market(s)

People looking to advance and improve themselves through a success coach

Industry/Entity Type

Life Coaching

Contact Information for Business Card

Contact information on card.
Business name on front of card
Questions on back

Font styles to use
Other font styles liked:
• Century Gothic or other Serif style fonts that look similar to Century Gothic

Colors

Designer to choose colors to be used in the design.

Requirements
Must have
• Logo on front of card
• Business name - The Steady Forge
• Contact name - Ted Harlow
• Address - Box 4619, Littleton, CO 80127-4619
• Phone number - 303-555-0147
• Email address - harlow.ted@thesteadyforge.example
• Certifications - CSC, CCHt, PTT, PNLP
• Back of card
• Three questions on the back of the card:
• If you were at your best, what would you do right now?
• What is the decision you have been avoiding?
• What's one action you could take in the next 10 minutes?
Nice to have
• I would like to see a solid color on the front of the card that compliments the logo.
• Back should be white, or could be contrasting, but need to have the three questions.

```html
<!DOCTYPE html>
<html lang="en">
<head>
<meta charset="utf-8">
<title>The Steady Forge – Business Card</title>
<link href="https://fonts.googleapis.com/css2?family=Questrial&family=Work+Sans:ital,wght@0,400;1,600&display=swap" rel="stylesheet">
<style>
  :root {
    --backdrop: #808080;
    --paper: #f8f8f9;
    --navy: #061634;
    --ink: #1c2a5c;
    --accent: #4a8fd8;
    --brand-muted: #2d4a8c;
    --white: #ffffff;
    --rule: #2a3766;
  }
  * { margin: 0; padding: 0; box-sizing: border-box; }
  html, body { width: 1200px; height: 1020px; overflow: hidden; }
  body { background: var(--backdrop); position: relative; font-family: "Questrial", "Century Gothic", sans-serif; }

  .card {
    position: absolute;
    left: 271px;
    width: 657px;
    height: 377px;
    box-shadow: 0 18px 30px rgba(0,0,0,0.35);
  }

  /* Back: questions */
  .card-back { top: 88px; background: var(--paper); color: var(--ink); }
  .questions-title {
    position: absolute; left: 21px; top: 24px;
    font-family: "Work Sans", sans-serif; font-style: italic; font-weight: 600;
    font-size: 23px; letter-spacing: 0.5px; color: var(--ink);
  }
  .question {
    position: absolute; left: 21px;
    font-family: "Work Sans", sans-serif; font-size: 16px; letter-spacing: 0.3px;
  }
  .answer-line {
    position: absolute; left: 22px; width: 495px; height: 0;
    border-top: 2px dotted var(--rule);
  }

  /* Front: identity */
  .card-front { top: 514px; height: 376px; background: var(--navy); color: var(--white); }
  .brand-name {
    position: absolute; left: 21px; top: 126px;
    font-size: 22px; color: var(--brand-muted); letter-spacing: 0.2px;
  }
  .person { position: absolute; right: 28px; top: 100px; text-align: right; }
  .person-name { font-size: 30px; color: var(--accent); letter-spacing: 0.5px; line-height: 1.2; }
  .person-certs { font-size: 20px; color: var(--white); margin-top: 4px; }
  .edge-tab {
    position: absolute; right: 0; top: 109px; width: 9px; height: 54px;
    background: var(--accent); border-radius: 4px 0 0 4px;
  }
  .contact-list { position: absolute; left: 20px; top: 240px; list-style: none; }
  .contact-item {
    display: flex; align-items: center; height: 30px; font-size: 20px; letter-spacing: 0.3px;
  }
  .contact-icon { width: 18px; height: 18px; margin-right: 9px; flex: none; }
</style>
</head>
<body>

<section class="card card-back">
  <h2 class="questions-title">Questions for you?</h2>
  <p class="question" style="top:80px">1. If you were at your best, what would you do right now?</p>
  <div class="answer-line" style="top:134px"></div>
  <p class="question" style="top:183px">2. What is the decision you have been avoiding?</p>
  <div class="answer-line" style="top:237px"></div>
  <p class="question" style="top:286px">3. What's one action you could take in the next 10 minutes?</p>
  <div class="answer-line" style="top:340px"></div>
</section>

<section class="card card-front">
  <div class="brand-name">The Steady Forge</div>

  <div class="person">
    <div class="person-name">Ted Harlow</div>
    <div class="person-certs">CSC, CCHt, PTT, PNLP</div>
  </div>
  <div class="edge-tab"></div>

  <ul class="contact-list">
    <li class="contact-item">
      <svg class="contact-icon" viewBox="0 0 24 24"><path fill="var(--accent)" d="M6.6 10.8a15 15 0 0 0 6.6 6.6l2.2-2.2a1 1 0 0 1 1-.25 11.4 11.4 0 0 0 3.6.57 1 1 0 0 1 1 1V20a1 1 0 0 1-1 1A17 17 0 0 1 3 4a1 1 0 0 1 1-1h3.5a1 1 0 0 1 1 1c0 1.25.2 2.45.57 3.57a1 1 0 0 1-.25 1z"/></svg>
      303-555-0147
    </li>
    <li class="contact-item">
      <svg class="contact-icon" viewBox="0 0 24 24"><rect x="3" y="6" width="18" height="12" rx="1" fill="var(--accent)"/><path d="M3 6l9 7 9-7" fill="none" stroke="var(--navy)" stroke-width="1.6"/></svg>
      harlow.ted@thesteadyforge.example
    </li>
    <li class="contact-item">
      <svg class="contact-icon" viewBox="0 0 24 24"><circle cx="12" cy="12" r="9" fill="var(--accent)"/><path d="M3 12h18M12 3c3 3 3 15 0 18M12 3c-3 3-3 15 0 18" fill="none" stroke="var(--navy)" stroke-width="1.4"/></svg>
      www.thesteadyforge.example
    </li>
    <li class="contact-item">
      <svg class="contact-icon" viewBox="0 0 24 24"><path fill="var(--accent)" d="M12 2a6 6 0 0 0-6 6c0 4.5 6 10 6 10s6-5.5 6-10a6 6 0 0 0-6-6zm0 8.2A2.2 2.2 0 1 1 12 5.8a2.2 2.2 0 0 1 0 4.4z"/><ellipse cx="12" cy="20.5" rx="7" ry="1.6" fill="none" stroke="var(--accent)" stroke-width="1.4"/></svg>
      Box 4619, Littleton, CO 80127-4619
    </li>
  </ul>
</section>

</body>
</html>
```